MR AG Flyer design

I’d like to redesign an A5, double-sided flyer for the company MR AG (www.mrag.lu). The text/content is available in a Word document.

```html
<!DOCTYPE html>
<html lang="de">
<head>
<meta charset="utf-8">
<title>MR AG Luzern – Flyer</title>
<link rel="stylesheet" href="https://fonts.googleapis.com/css2?family=Poppins:ital,wght@0,400;0,500;0,600;0,700;0,800;1,400;1,500&display=swap">
<style>
  :root {
    --navy: #263f93;
    --navy-deep: #2b3873;
    --orange: #f4a024;
    --orange-hot: #f0782a;
    --grey: #d6d6d6;
    --white: #ffffff;
    --paper: #ffffff;
  }
  * { margin: 0; padding: 0; box-sizing: border-box; }
  html, body { width: 842px; height: 1200px; overflow: hidden; background: var(--paper); }
  body { position: relative; font-family: "Poppins", sans-serif; color: var(--white); }

  .flyer { position: absolute; left: 98px; top: 66px; width: 652px; height: 925px; overflow: hidden; }
  .flyer-art { position: absolute; inset: 0; width: 100%; height: 100%; }

  .abs { position: absolute; }

  .brand { left: 66px; top: 26px; display: flex; align-items: center; gap: 12px; }
  .brand-mark { width: 24px; height: 28px; background: var(--white); }
  .brand-name { font-size: 21px; font-weight: 700; color: var(--white); letter-spacing: 0.2px; }

  .title { left: 23px; top: 218px; font-size: 58px; font-weight: 800; line-height: 42px; color: var(--navy); letter-spacing: -1px; }

  .intro { left: 26px; top: 441px; width: 400px; }
  .intro h2 { font-size: 22px; font-weight: 700; line-height: 29px; }
  .intro p { margin-top: 8px; font-size: 14.5px; line-height: 19px; font-weight: 500; }

  .service { left: 26px; width: 410px; }
  .service-solar { top: 567px; }
  .service-effizienz { top: 733px; }
  .service h3 { font-size: 19.5px; font-weight: 500; line-height: 26px; }
  .service .claim { margin-top: 2px; font-size: 15px; font-style: italic; font-weight: 500; line-height: 22px; }
  .service ul { list-style: none; margin-top: 10px; font-size: 12.4px; line-height: 19px; font-weight: 500; }
  .service li { padding-left: 7px; text-indent: -7px; }
  .service li::before { content: "• "; }
  .service li .more { display: block; padding-left: 1px; text-indent: 0; }

  .benefit { right: 20px; font-size: 20.5px; font-weight: 500; line-height: 22px; text-align: right; }
  .benefit-1 { top: 362px; }
  .benefit-2 { top: 463px; }
  .benefit-3 { top: 550px; }

  .cta { left: 433px; top: 690px; width: 200px; text-align: center; font-size: 23px; font-weight: 800; line-height: 24.5px; }
  .contact-note { left: 433px; top: 856px; width: 200px; text-align: center; font-size: 15px; font-weight: 700; line-height: 21px; }

  .message { position: absolute; left: 0; width: 842px; text-align: center; color: var(--navy); font-weight: 700; font-size: 27px; line-height: 34px; letter-spacing: -0.4px; }
  .message-draft { top: 1030px; }
  .message-thanks { top: 1130px; }
</style>
</head>
<body>
  <section class="flyer">
    <svg class="flyer-art" viewBox="0 0 1240 1757" preserveAspectRatio="none" aria-hidden="false">
      <defs>
        <linearGradient id="photoTone" x1="1" y1="0" x2="0" y2="1">
          <stop offset="0" stop-color="#f3d9b8"/>
          <stop offset="0.3" stop-color="#9b8a5c"/>
          <stop offset="0.6" stop-color="#5d6478"/>
          <stop offset="1" stop-color="#8a8a45"/>
        </linearGradient>
        <linearGradient id="orangeSweep" x1="0" y1="0" x2="1" y2="0">
          <stop offset="0" stop-color="#f4a024"/>
          <stop offset="1" stop-color="#f07a24"/>
        </linearGradient>
        <linearGradient id="pillFill" x1="0" y1="0" x2="1" y2="0">
          <stop offset="0" stop-color="#f4a024"/>
          <stop offset="1" stop-color="#f0752a"/>
        </linearGradient>
        <linearGradient id="ctaFill" x1="0" y1="1" x2="1" y2="0">
          <stop offset="0" stop-color="#f07025"/>
          <stop offset="1" stop-color="#f4a524"/>
        </linearGradient>
      </defs>

      <rect width="1240" height="1757" fill="var(--white)"/>

      <path role="img" aria-label="Foto: Hausdach mit Solarmodulen im Abendlicht" d="M1030 0 H1240 V880 H415 C430 500 560 280 1030 0 Z" fill="url(#photoTone)"/>

      <path d="M0 0 H842 C760 120 650 190 560 195 C400 200 200 180 0 155 Z" fill="var(--navy)"/>
      <path d="M842 0 H880 C800 130 700 185 600 196 C700 180 780 110 842 0 Z" fill="var(--grey)"/>
      <path d="M0 154 C200 180 420 200 600 195 C790 180 940 90 1032 0 L1040 0 C920 130 740 230 560 262 C360 300 160 340 0 350 Z" fill="url(#orangeSweep)"/>
      <path d="M548 250 C470 380 432 520 415 680 L432 680 C450 520 500 380 610 236 Z" fill="var(--orange-hot)"/>

      <path d="M0 760 C150 690 350 660 520 675 C760 700 920 800 1240 840 V900 H0 Z" fill="var(--orange)"/>
      <path d="M0 760 C150 710 300 705 420 720 C280 725 140 740 0 762 Z" fill="var(--grey)"/>
      <path d="M0 830 C180 730 470 730 660 810 C820 880 960 980 1240 1000 V1740 H0 Z" fill="var(--navy)"/>
      <path d="M900 1000 L1240 1000 V1620 L1120 1500 Z" fill="var(--navy-deep)" opacity="0.55"/>
      <path d="M1140 1140 L1240 1140 V1240 Z" fill="var(--orange)"/>
      <rect x="0" y="1376" width="830" height="364" fill="var(--navy-deep)"/>
      <rect x="0" y="1740" width="1240" height="17" fill="url(#orangeSweep)"/>

      <g stroke="var(--white)" stroke-width="3" fill="url(#pillFill)">
        <path d="M1240 664 H918 A74 74 0 0 0 918 812 H1240"/>
        <path d="M1240 829 H918 A74 74 0 0 0 918 976 H1240"/>
        <path d="M1240 996 H918 A73 73 0 0 0 918 1142 H1240"/>
      </g>

      <circle cx="1014" cy="1404" r="192" fill="url(#ctaFill)"/>
      <circle cx="1014" cy="1404" r="180" fill="none" stroke="var(--white)" stroke-width="3"/>
    </svg>

    <div class="abs brand">
      <span class="brand-mark"></span>
      <span class="brand-name">MR AG Luzern</span>
    </div>

    <h1 class="abs title">MR AG<br>Luzern</h1>

    <div class="abs intro">
      <h2>Solarenergie &amp; Energieeffizienz aus einer Hand</h2>
      <p>Wir planen und beraten rund um Photovoltaik und Energieeffizienz – für Private, Gewerbe und Industrie.</p>
    </div>

    <div class="abs service service-solar">
      <h3>Solar Energie</h3>
      <p class="claim">Photovoltaik-Lösungen, die zu Ihrem Dach passen</p>
      <ul>
        <li>Indach PV-Anlagen (integriert &amp; ästhetisch)</li>
        <li>Aufdach PV-Anlagen (effizient &amp; preis-/leistungsstark)</li>
        <li>Eigenverbrauch optimieren <span class="more">(Batterie, Wärmepumpe, E-Mobility, smartes Lastmanagement)</span></li>
      </ul>
    </div>

    <div class="abs service service-effizienz">
      <h3>Energie Effizie</h3>
      <p class="claim">Beratung &amp; Konzepte für nachhaltige Gebäude</p>
      <ul>
        <li>Energieberatung / GEAK / GEAK Plus</li>
        <li>Impulsberatung &amp; Energiekonzept <span class="more">(HLK + PV, Simulationen, Nachweise)</span></li>
        <li>Energiesanierung <span class="more">(Planung, Koordination, Förderabwicklung)</span></li>
      </ul>
    </div>

    <p class="abs benefit benefit-1">Mehr<br>Eigenverbrauch</p>
    <p class="abs benefit benefit-2">Mehr Effizienz</p>
    <p class="abs benefit benefit-3">Mehr Zukunft</p>

    <p class="abs cta">Jetzt<br>unverbindlich<br>Kontakt<br>aufnehmen</p>
    <p class="abs contact-note">Telefon oder E-Mail<br>wir melden uns zeitnah.</p>
  </section>

  <p class="message message-draft">Hi, Here is a draft flyer design.<br>Let me know your feedback to complete the rest.</p>
  <p class="message message-thanks">Thank you! Have a nice day!</p>
</body>
</html>
```